Homepage Redesign for Healthcare Tech Company

This is for a redesign of our current homepage. We have specific notes and a Mockup and we need a great designer to bring it to life and make it look sophisticated and professional. Please see the Current Page (attached and online) as well as the Notes doc and Mockup PPT, both attached, for what we need.

Overall, look at the current page as a sketch of what it could be. We would like a design that really nails the structure of both the overall page and the pipeline (that runs through Sections 1-4), so that it looks like one, clean, custom design (not pieced together). It’s important that the basic structure of the pipeline, especially the transition from icons to screenshots (starting in section 2, and mostly in section 3) all flow together well and look like a deliberate, well thought-out design. Please include that, and at least the headlines for each section, in any initial submissions.

We will be building out of website beyond just this page, and would be great to work with a designer we can continue working with on the website, the graphical screenshots and some infographics. Not a must but definitely an option if you would like. We didn’t include all pages in this project, because we would like the designer to focus all energy on creating a well thought-out homepage design with the wow factor, and we can build it out together from there. For now, we would like just 2 additional general theme pages (one smaller page for a couple paragraphs of text only and one with a few uniform sections, with room for text and small graphic-see notes).

Our customers are healthcare companies – both Doctors and IT professionals of medium to large healthcare organizations who support doctors. We are experts in healthcare interoperability technology and the page should reflect that. Medical Record documentation is an expensive time-consuming massive headache for our customer base. What we are offering is a truly groundbreaking solution that leverages the best technology available to bring them something that wasn’t possible before – ALL of their patient data in one enriched and linked document, delivered to their current workflow. It's an expensive solution but very impactful in terms of better patient care and dramatically streamlined workflow - the homepage needs to reflect that. Please take the time to understand the solution we offer and just let me know if you need clarification – I’m happy to answer any questions.

Thanks!

SEE ATTACHMENTS, and also this more detailed breakdown of the sections: https://qx.lnk/Rt4mPa

Target Market(s)

Doctors, IT Professionals in the Healthcare field, Medical Coders..but focus should be on Doctors

Number of Pages Required

1 page

Colors
0355a3
3276b5
0293ce
6b449b
886aae
b7a5cd
00a990
33b8a4
86cfc6

Requirements
Must have
• - Sophisticated, professional, masterful layout
- Must refer to the attached DESIGN NOTES.doc (about 2 pages) and MOCKUP.PPT but bring the idea to life in an innovative way. In general, we collect all medical records, summarize and unify into 1 document that we send straight into each patient file, but referring to the actual notes to truly get what we do and what we need it is a must.
- Framing/background emphasis for provided screenshots (even if these screenshots don't fit exactly, we will make them fit after)
- Emphasis on the fact that clicking the View Source buttons in the Brightfold (what we call our product) opens the actual source documents (underlying medical record) - this is a big deal for doctors and medical coders.
- Final design should be in editable PSD file
Nice to have
• Animation. We are asking for design only because we want the best design possible but we would definitely choose a great animated design (assuming that means you'd need to code it too - let me know) and ensure that you are paid the extra for coding if you need to code it yourself.
Should not have
• template feel - should look custom
cheesy photos of models dressed as doctors

```html
<!DOCTYPE html>
<html lang="en">
<head>
<meta charset="utf-8">
<title>Vantora — Unified Clinical Intelligence</title>
<link href="https://fonts.googleapis.com/css2?family=Lato:wght@300;400;700&family=Mulish:wght@300;400;600;700&display=swap" rel="stylesheet">
<style>
:root{
  --ink:#05070a;
  --panel-a:#1b2733;
  --panel-b:#0d141c;
  --text:#ffffff;
  --muted:#7f8c99;
  --soft:#b9c3cc;
  --purple:#6b449b;
  --purple-l:#886aae;
  --lilac:#b7a5cd;
  --blue:#3276b5;
  --sky:#0293ce;
  --teal:#00a990;
  --teal-l:#33b8a4;
  --mint:#86cfc6;
  --line:#2a3744;
}
*{box-sizing:border-box;margin:0;padding:0}
html,body{width:1200px;height:4194px;overflow:hidden;background:var(--ink)}
body{font-family:"Lato",sans-serif;color:var(--text);position:relative}
.page{position:relative;width:1200px;height:4194px}
section,header,footer{position:relative;width:1200px}
.abs{position:absolute}
h2.title{font-family:"Mulish",sans-serif;font-weight:600;font-size:21px;letter-spacing:.2px;text-transform:uppercase}
.muted{color:var(--muted)}
.panel{position:absolute;left:41px;width:1118px;background:linear-gradient(180deg,var(--panel-a),var(--panel-b))}
.btn{display:inline-block;border:1px solid #5a6470;color:#d8dde2;font-size:13px;padding:9px 14px;border-radius:2px}
.brand{display:flex;align-items:center;gap:9px;font-family:"Mulish",sans-serif;font-weight:600;font-size:25px;letter-spacing:1px;color:#dfe6ee}
.brand i{display:block;width:20px;height:20px;background:var(--purple-l)}

/* hero */
.hero{height:619px;overflow:hidden}
.hero-bg{position:absolute;inset:0;background:radial-gradient(ellipse at 35% 55%,#6b6870 0%,#3c3d46 35%,#1f2430 65%,#05070a 100%)}
.nav{position:absolute;top:46px;left:130px;right:130px;display:flex;align-items:center;justify-content:space-between;font-size:13px;color:#d4d8dd}
.nav .links{display:flex;gap:22px;width:260px}
.nav .right{display:flex;gap:28px;align-items:center;width:260px;justify-content:flex-end}
.nav .brand{position:absolute;left:50%;transform:translateX(-50%)}
.hero-copy{position:absolute;top:262px;width:100%;text-align:center}
.hero-copy h1{font-family:"Mulish",sans-serif;font-weight:300;font-size:45px;letter-spacing:.3px}
.hero-copy p{font-family:"Mulish",sans-serif;font-weight:600;font-size:19px;line-height:23px;color:#e0e3e8;margin-top:14px}
.cta{display:inline-block;margin-top:40px;background:var(--purple);color:#fff;font-size:13px;padding:10px 17px}

.intro{height:185px}
.intro p{position:absolute;top:64px;left:160px;width:880px;text-align:center;font-size:16px;line-height:22px;font-family:"Mulish",sans-serif}

/* network */
.network{height:609px}
.network .panel{top:0;height:609px}
.net-head{position:absolute;left:89px;top:38px}
.net-head p{font-family:"Mulish",sans-serif;font-weight:600;font-size:18px;color:var(--muted);margin-top:6px}
.net-label{position:absolute;top:124px;width:100%;text-align:center;font-family:"Mulish",sans-serif;font-weight:700;font-size:20px}
.source{position:absolute;width:320px}
.source h3{font-family:"Mulish",sans-serif;font-weight:600;font-size:16px;margin-bottom:12px}
.source p{font-size:12.5px;line-height:14.5px;color:var(--muted)}
.node{position:absolute;width:48px;height:48px;border-radius:50%;background:#05070a;display:flex;align-items:center;justify-content:center}

/* pipeline */
.pipe{position:absolute;left:599px;width:2px}

/* transform */
.transform{height:451px}
.tf-copy{position:absolute;left:130px;top:142px;width:350px}
.tf-copy h2{font-family:"Mulish",sans-serif;font-weight:600;font-size:20px;line-height:25px}
.tf-copy p{font-size:12.5px;line-height:15px;color:#c3c9cf;margin-top:26px}
.hub{position:absolute;left:542px;top:179px;width:116px;height:116px;border-radius:50%;border:2px solid #0e5b54;box-shadow:0 0 30px rgba(0,169,144,.35);display:flex;align-items:center;justify-content:center;background:#05070a}
.hub span{width:60px;height:60px;border-radius:50%;border:1px solid #2c4652;display:flex;align-items:center;justify-content:center}
.caption{position:absolute;left:723px;top:324px;width:335px;font-size:12.5px;line-height:15px;color:#c3c9cf}

/* doc mocks */
.doc{position:absolute;background:#fff;color:#1a2530;overflow:hidden;font-family:"Lato",sans-serif}
.doc .bar{height:4px;background:#c6ccd3;border-radius:1px;margin:3px 0}
.doc .row{height:1px;background:#d5dadf;margin:7px 0}
.doc-head{display:flex;justify-content:space-between;align-items:center;font-size:8px;font-weight:700;padding:4px 6px}
.doc-head .mk{display:flex;align-items:center;gap:4px;color:#22334a}
.doc-head .mk i{width:7px;height:7px;background:var(--purple-l)}
.doc h5{font-size:9px;font-weight:700;margin:6px 6px 3px}
.doc .grid{display:flex;gap:8px;padding:0 6px}
.doc .grid .bar{flex:1;height:3px;background:#9aa4ae}
.framed{border:3px solid #d7dde4;box-shadow:0 6px 20px rgba(0,0,0,.5)}
.lines{padding:4px 6px}
.lines .ln{display:flex;gap:6px;align-items:center;height:12px;border-bottom:1px solid #e6e9ec}
.lines .ln b{width:20px;height:3px;background:var(--teal-l)}
.lines .ln u{flex:1;height:3px;background:#b8bfc6;text-decoration:none}
.lines .ln s{width:14px;height:3px;background:var(--teal)}

/* summary */
.summary{height:557px}
.summary .panel{top:0;height:557px}
.sum-head{position:absolute;left:89px;top:40px;width:960px}
.sum-head p{font-size:12.5px;line-height:15px;color:var(--soft);margin-top:10px}
.divider{position:absolute;left:89px;right:40px;top:135px;height:1px;background:var(--line)}
.col{position:absolute;top:177px;width:330px}
.col h3{font-family:"Mulish",sans-serif;font-weight:400;font-size:17px}
.col p{font-size:12.5px;line-height:15px;color:var(--muted);margin-top:14px}
.arrows{position:absolute;display:flex;gap:12px;align-items:center}
.arrows .sep{width:1px;height:20px;background:#3e4a56}

/* delivered */
.delivered{height:534px}
.del-head{position:absolute;left:130px;top:86px}
.del-head p{font-size:12.5px;line-height:16px;color:var(--soft);margin-top:10px}
.vdiv{position:absolute;left:553px;top:195px;width:1px;height:250px;background:#22303d}
.tile{position:absolute;width:146px;height:79px;background:#0b1118;border:1px solid #151f29;display:flex;align-items:center;justify-content:center;font-family:"Mulish",sans-serif;font-weight:600;font-size:20px;color:#dfe4ea}

/* features */
.features{height:272px}
.features .panel{top:0;height:272px}
.feat{position:absolute;top:75px;width:205px}
.feat h3{font-family:"Mulish",sans-serif;font-weight:400;font-size:16px;text-transform:uppercase;margin-top:30px}
.feat p{font-size:12.5px;line-height:15px;color:var(--muted);margin-top:10px}

/* blogs */
.blogs{height:493px}
.blogs h2{position:absolute;top:66px;width:100%;text-align:center;font-family:"Mulish",sans-serif;font-weight:400;font-size:20px}
.card{position:absolute;top:127px;width:441px;height:329px;background:linear-gradient(180deg,#19232d,#0f161d)}
.card .media{height:187px;background:linear-gradient(135deg,#c9d3dc,#7d8c99 55%,#3d4a57)}
.card p{font-size:12.5px;line-height:18px;color:var(--muted);margin:35px 24px 0}
.card .meta{font-size:12.5px;color:#c9ced3;margin:22px 24px 0;display:flex;gap:25px}
.card .meta a{color:var(--purple-l);text-decoration:underline}

.closing{height:208px}
.closing p{position:absolute;left:174px;width:860px;font-size:13px;line-height:17px}

/* footer */
.footer{height:266px;background:#0c1218}
.f-nav{position:absolute;top:28px;left:130px;display:flex;gap:28px;font-size:13px;color:#c9ced3}
.footer .btn{position:absolute;right:130px;top:24px}
.f-rule{position:absolute;top:82px;left:130px;right:130px;height:1px;background:#1f2a35}
.f-links{position:absolute;top:128px;font-size:12.5px;line-height:26px;color:#c9ced3}
.copy{position:absolute;top:222px;left:130px;font-size:11px;color:var(--muted)}
.f-mark{position:absolute;left:1044px;top:212px;width:24px;height:24px;background:var(--purple-l)}
</style>
</head>
<body>
<div class="page">

<!-- pipeline spine -->
<div class="pipe" style="top:1035px;height:380px;background:linear-gradient(180deg,#3a3f78,#3a3f78)"></div>
<div class="pipe" style="top:1415px;height:449px;background:linear-gradient(180deg,#3a3f78,#0d6d64 45%,#0d6d64)"></div>

<header class="hero">
  <div class="hero-bg" role="img" aria-label="Softly lit photograph of a clinician reviewing records, overlaid with a faint data network"></div>
  <nav class="nav">
    <div class="links"><span>About</span><span>Features</span><span>Process</span><span>Team</span></div>
    <div class="brand"><i></i>VANTORA</div>
    <div class="right"><span>Clients</span><span class="btn">Request Access</span></div>
  </nav>
  <div class="hero-copy">
    <h1>Unified Clinical Intelligence</h1>
    <p>Each patients' full medical history, summary and analysis in one<br>comprehensive health record</p>
    <span class="cta">Request Access</span>
  </div>
</header>

<section class="intro">
  <p>Vantora collects patients' records from all sources of external clinical data, synthesizes the captured data into one composite health record, abstracts all HCC, MIPS and HEDIS opportunities, and delivers them directly into your EHR, all in a matter of hours.</p>
</section>

<section class="network">
  <div class="panel">
    <div class="net-head">
      <h2 class="title">Your patients' full medical history from all sources</h2>
      <p>Vantora clinical data network has unprecedented reach across the continuum of care.</p>
    </div>
    <div class="net-label">VANTORA CLINICAL DATA NETWORK</div>

    <svg class="abs" style="left:0;top:0" width="1118" height="609" aria-hidden="true">
      <g stroke="#4a5fa8" stroke-width="1.5" stroke-dasharray="2 4" fill="none">
        <line x1="470" y1="248" x2="558" y2="259"/>
        <line x1="628" y1="246" x2="558" y2="294"/>
        <line x1="470" y1="360" x2="558" y2="351"/>
        <line x1="628" y1="360" x2="558" y2="400"/>
        <line x1="470" y1="483" x2="558" y2="505"/>
        <line x1="628" y1="468" x2="558" y2="451"/>
      </g>
      <g fill="#5b78d6">
        <circle cx="558" cy="259" r="3"/><circle cx="558" cy="294" r="3"/><circle cx="558" cy="351" r="3"/>
        <circle cx="558" cy="400" r="3"/><circle cx="558" cy="451" r="3"/><circle cx="558" cy="505" r="3"/>
      </g>
    </svg>

    <div class="source" style="left:89px;top:226px"><h3>EMR Networks</h3><p>Connected to 800,000 Physician<br>EMR databases and over 60,000<br>hospitals across the country.</p></div>
    <div class="source" style="left:89px;top:335px"><h3>RX Data or US Pharmacies</h3><p>Comprehensive medication history including medication starts, adherence, and switching behavior is collected from national and regional pharmacy data feeds. This includes specialized pharmacies.</p></div>
    <div class="source" style="left:89px;top:458px"><h3>Diagnostic Labs</h3><p>Vantora is directly connected to all major<br>diagnostic testing laboratories, enabling<br>collection of all lab results.</p></div>
    <div class="source" style="left:703px;top:226px"><h3>HIE Networks</h3><p>Aggregating from 32 Health<br>Information Exchange networks for<br>real-time access to clinical data.</p></div>
    <div class="source" style="left:703px;top:335px"><h3>Provider Faxes</h3><p>Fax records received from PCPs and specialists are converted into structured, searchable electronic records (C-CD) for ingestion into the Vantora Brightfold™.</p></div>
    <div class="source" style="left:703px;top:458px"><h3>Claims Databases</h3><p>Connected to the nation's largest clearinghouses for open and closed claims submission and processing, including Medicare Part A, B and D data for 53 million Medicare beneficiaries. This includes Medical &amp; Rx Open/Closed Claims EDI and Remittance ERI.</p></div>

    <div class="node" style="left:419px;top:224px"><svg width="20" height="20" viewBox="0 0 20 20" fill="none" stroke="#fff" stroke-width="1.8"><rect x="3" y="3" width="14" height="11"/><path d="M10 6v5M7.5 8.5 10 11l2.5-2.5M3 17h14"/></svg></div>
    <div class="node" style="left:419px;top:340px"><svg width="20" height="20" viewBox="0 0 20 20" fill="none" stroke="#fff" stroke-width="1.6"><path d="M5 2h7l3 3v13H5z"/><path d="M8 8h3a1.5 1.5 0 0 1 0 3H8V8m0 3v4m2-4 3 4"/></svg></div>
    <div class="node" style="left:419px;top:455px"><svg width="20" height="20" viewBox="0 0 20 20" fill="none" stroke="#fff" stroke-width="1.8"><path d="M4 16l1-4 8-8 3 3-8 8zM12 5l3 3"/></svg></div>
    <div class="node" style="left:627px;top:224px"><svg width="20" height="20" viewBox="0 0 20 20" fill="none" stroke="#fff" stroke-width="1.8"><path d="M3 7h13m-3-3 3 3-3 3M17 13H4m3-3-3 3 3 3"/></svg></div>
    <div class="node" style="left:627px;top:340px"><svg width="20" height="20" viewBox="0 0 20 20" fill="#fff"><rect x="3" y="5" width="4" height="12"/><rect x="8" y="3" width="9" height="14"/><rect x="10" y="6" width="2" height="2" fill="#05070a"/><rect x="13" y="6" width="2" height="2" fill="#05070a"/><rect x="10" y="10" width="2" height="2" fill="#05070a"/><rect x="13" y="10" width="2" height="2" fill="#05070a"/></svg></div>
    <div class="node" style="left:627px;top:447px"><svg width="24" height="24" viewBox="0 0 24 24"><circle cx="12" cy="12" r="10" fill="#cfd5db"/><path d="M7 12l3.5 3.5L17 9" stroke="#05070a" stroke-width="2" fill="none"/></svg></div>
  </div>
</section>

<section class="transform">
  <div class="tf-copy">
    <h2>TRANSFORMED INTO<br>1 COMPOSITE<br>C-CDA HEATH RECORD</h2>
    <p>The Vantora synthesis engine utilizes OCR, advanced parsing techniques, Clinical Natural Language Processing (cNLP), proprietary logic and NPI matching to clean, de-duplicate, structure and enrich all inputs from data acquisition.</p>
  </div>
  <div class="hub"><span><svg width="30" height="30" viewBox="0 0 30 30" fill="none" stroke="#8e9aa6" stroke-width="1.2"><rect x="5" y="5" width="20" height="20"/><path d="M5 5l20 20M25 5 5 25"/><rect x="10" y="10" width="10" height="10" transform="rotate(45 15 15)"/></svg></span></div>
  <div class="doc" style="left:723px;top:88px;width:333px;height:213px">
    <div class="doc-head"><span class="mk"><i></i>VANTORA</span><span>C-CDA</span><span>Doe, John</span></div>
    <div style="margin:2px 6px 0 200px;height:6px;border:1px solid #c6ccd3"></div>
    <h5>Insurance Providers</h5><div class="row"></div><div class="grid"><span class="bar"></span><span class="bar"></span><span class="bar"></span><span class="bar"></span><span class="bar"></span><span class="bar"></span></div><div class="row"></div>
    <h5>Medications</h5><div class="row"></div><div class="grid"><span class="bar"></span><span class="bar"></span><span class="bar"></span><span class="bar"></span><span class="bar"></span><span class="bar"></span><span class="bar"></span></div><div class="row"></div>
    <h5>Results</h5><div class="row"></div><div class="grid"><span class="bar"></span><span class="bar"></span><span class="bar"></span><span class="bar"></span></div><div class="row"></div>
    <h5>Problems</h5><div class="row"></div><div class="grid"><span class="bar"></span><span class="bar"></span><span class="bar"></span><span class="bar"></span><span class="bar"></span><span class="bar"></span></div>
  </div>
  <p class="caption">The normalized data is unified into the Brightfold C-CDA, an enhanced composite longitudinal record in C-CDA format, the industry standard for all interoperability initiatives</p>
</section>

<section class="summary">
  <div class="panel">
    <div class="sum-head">
      <h2 class="title">Summarized and linked to key insights</h2>
      <p>Insights are presented in a concise summary with direct links to supporting evidence. HCC, HEDIS and MIPS opportunities are abstracted and cross-linked directly to the original text in the underlying record for quick and easy reference.</p>
    </div>
    <div class="divider"></div>
    <div class="col" style="left:89px"><h3>Risk-Adjustment</h3><p>HCC opportunities for new capture and recapture are identified and extracted using logic algorithms.</p></div>
    <div class="col" style="left:680px"><h3>Quality Analysis</h3><p>HEDIS and MIPS quality measure gaps closed using NCQA certified technology to generate QRDAIII.</p></div>

    <div class="doc framed" style="left:89px;top:267px;width:295px;height:197px">
      <div class="doc-head"><span class="mk"><i></i>VANTORA</span><span>Brightfold™</span><span>Doe, John</span></div>
      <div class="lines"><div class="ln"><b></b><u></u><s></s></div><div class="ln"><b></b><u></u><s></s></div><div class="ln"><b></b><u></u><s></s></div><div class="ln"><b></b><u></u><s></s></div><div class="ln"><b></b><u></u><s></s></div><div class="ln"><b></b><u></u><s></s></div><div class="ln"><b></b><u></u><s></s></div><div class="ln"><b></b><u></u><s></s></div><div class="ln"><b></b><u></u><s></s></div><div class="ln"><b></b><u></u><s></s></div><div class="ln"><b></b><u></u><s></s></div></div>
    </div>
    <div class="doc framed" style="left:410px;top:267px;width:295px;height:197px">
      <div class="lines"><div class="ln"><b></b><u></u><s></s></div><div class="ln"><b></b><u></u><s></s></div><div class="ln"><b></b><u></u><s></s></div><div class="ln"><b></b><u></u><s></s></div><div class="ln"><b></b><u></u><s></s></div><div class="ln"><b></b><u></u><s></s></div><div class="ln"><b></b><u></u><s></s></div><div class="ln"><b></b><u></u><s></s></div><div class="ln"><b></b><u></u><s></s></div><div class="ln"><b></b><u></u><s></s></div><div class="ln"><b></b><u></u><s></s></div><div class="ln"><b></b><u></u><s></s></div></div>
    </div>
    <div class="doc framed" style="left:731px;top:267px;width:296px;height:197px">
      <div class="doc-head"><span class="mk"><i></i>VANTORA</span><span>C-CDA</span><span>Doe, John</span></div>
      <h5>Medications</h5>
      <div class="lines"><div class="ln"><u></u><u></u><u></u></div><div class="ln"><u></u><u></u><u></u></div><div class="ln"><u></u><u></u><u></u></div><div class="ln"><u></u><u></u><u></u></div><div class="ln"><u></u><u></u><u></u></div><div class="ln"><u></u><u></u><u></u></div><div class="ln"><u></u><u></u><u></u></div><div class="ln"><u></u><u></u><u></u></div><div class="ln"><u></u><u></u><u></u></div><div class="ln"><u></u><u></u><u></u></div></div>
    </div>

    <div class="arrows" style="left:530px;top:499px">
      <svg width="16" height="12" viewBox="0 0 16 12" fill="none" stroke="#3a5a57" stroke-width="1.8"><path d="M15 6H2m4-4L2 6l4 4"/></svg>
      <span class="sep"></span>
      <svg width="16" height="12" viewBox="0 0 16 12" fill="none" stroke="#33b8a4" stroke-width="1.8"><path d="M1 6h13m-4-4 4 4-4 4"/></svg>
    </div>
  </div>
</section>

<section class="delivered">
  <div class="del-head">
    <h2 class="title">Delivered directly into your EHR for native viewing</h2>
    <p>The final package is delivered as a single longitudinal record into each patient's chart within your EHR, viewable natively<br>The Vantora Brightfold is compatible with any Meaningful Use certified EHR.</p>
  </div>
  <div class="doc framed" style="left:133px;top:195px;width:388px;height:253px">
    <div class="doc-head" style="padding:8px 10px"><span class="mk"><i></i>VANTORA</span><span>HCC Brightfold™</span><span>Doe, John</span></div>
    <div class="lines" style="padding:6px 10px"><div class="ln"><b></b><u></u><s></s></div><div class="ln"><b></b><u></u><s></s></div><div class="ln"><b></b><u></u><s></s></div><div class="ln"><b></b><u></u><s></s></div><div class="ln"><b></b><u></u><s></s></div><div class="ln"><b></b><u></u><s></s></div><div class="ln"><b></b><u></u><s></s></div><div class="ln"><b></b><u></u><s></s></div><div class="ln"><b></b><u></u><s></s></div><div class="ln"><b></b><u></u><s></s></div><div class="ln"><b></b><u></u><s></s></div><div class="ln"><b></b><u></u><s></s></div><div class="ln"><b></b><u></u><s></s></div><div class="ln"><b></b><u></u><s></s></div><div class="ln"><b></b><u></u><s></s></div></div>
  </div>
  <div class="vdiv"></div>
  <div class="tile" style="left:589px;top:195px">Meridix</div>
  <div class="tile" style="left:760px;top:195px">Helixa</div>
  <div class="tile" style="left:915px;top:195px">Corvane</div>
  <div class="tile" style="left:589px;top:290px">Opalis</div>
  <div class="tile" style="left:760px;top:290px">Fernway</div>
  <div class="tile" style="left:915px;top:290px">Tessara</div>
  <div class="arrows" style="left:589px;top:414px;gap:24px">
    <svg width="16" height="12" viewBox="0 0 16 12" fill="none" stroke="#3e4a56" stroke-width="1.8"><path d="M15 6H2m4-4L2 6l4 4"/></svg>
    <svg width="16" height="12" viewBox="0 0 16 12" fill="none" stroke="#8a96a2" stroke-width="1.8"><path d="M1 6h13m-4-4 4 4-4 4"/></svg>
  </div>
</section>

<section class="features">
  <div class="panel">
    <div class="feat" style="left:89px">
      <svg width="36" height="36" viewBox="0 0 36 36" fill="none"><circle cx="18" cy="18" r="16" stroke="#33b8a4" stroke-width="2"/><circle cx="18" cy="18" r="10" stroke="#886aae" stroke-width="1.5"/><rect x="15" y="15" width="6" height="6" fill="#fff" transform="rotate(45 18 18)"/></svg>
      <h3>1-Click Access</h3><p>1-click access to each inference and insight in the underlying record</p>
    </div>
    <div class="feat" style="left:333px">
      <svg width="36" height="36" viewBox="0 0 36 36" fill="none"><path d="M30 12a14 14 0 1 1-20-5" stroke="#33b8a4" stroke-width="2"/><circle cx="18" cy="18" r="9" stroke="#886aae" stroke-width="1.5"/><rect x="15" y="15" width="6" height="6" fill="#fff" transform="rotate(45 18 18)"/></svg>
      <h3>Searchable</h3><p>All data in the Brightfold CCDA is searchable, including previously unstructured data</p>
    </div>
    <div class="feat" style="left:579px">
      <svg width="36" height="36" viewBox="0 0 36 36" fill="none"><circle cx="18" cy="18" r="16" stroke="#886aae" stroke-width="2"/><circle cx="18" cy="18" r="10" stroke="#33b8a4" stroke-width="1.5"/><rect x="15" y="15" width="6" height="6" fill="#fff" transform="rotate(45 18 18)"/></svg>
      <h3>Seamless Integration</h3><p>Designed for seamless integration into your current tools and workflow</p>
    </div>
    <div class="feat" style="left:823px">
      <svg width="36" height="36" viewBox="0 0 36 36" fill="none" stroke-width="2"><path d="M18 3v7M18 26v7M3 18h7M26 18h7" stroke="#886aae"/><path d="M8 8l4 4M24 24l4 4M28 8l-4 4M8 28l4-4" stroke="#33b8a4"/><rect x="15" y="15" width="6" height="6" fill="#fff" transform="rotate(45 18 18)"/></svg>
      <h3>Empower Physicians</h3><p>Provide physicians with a complete summarized medical history linked to supporting documentation ahead of every</p>
    </div>
  </div>
</section>

<section class="blogs">
  <h2>BLOGS</h2>
  <article class="card" style="left:147px">
    <div class="media" role="img" aria-label="Blog photo: two clinicians reviewing documents together"></div>
    <p>Vantora is committed to continually recruiting the most powerful technological tools and delivering...</p>
    <div class="meta"><span>February 26, 2020</span><a>Read More</a></div>
  </article>
  <article class="card" style="left:612px">
    <div class="media" role="img" aria-label="Blog photo: two clinicians reviewing documents together"></div>
    <p>Vantora is committed to continually recruiting the most powerful technological tools and delivering...</p>
    <div class="meta"><span>February 26, 2020</span><a>Read More</a></div>
  </article>
</section>

<section class="closing">
  <p style="top:40px">The Vantora Brightfold is a game-changing tool designed to accelerate success in value-based contracts by maximizing outcomes, scores and revenue while significantly decreasing inefficiencies and administrative burden.</p>
  <p style="top:90px">Vantora platform has been shaped by our partnerships with the leaders in value-based care to address their most complex challenges. We are experts in interoperability technology who are passionate about empowering healthcare organizations to achieve market-leading results.</p>
</section>

<footer class="footer">
  <div class="f-nav"><span>About</span><span>Features</span><span>Process</span><span>Team</span></div>
  <span class="btn">Request Access</span>
  <div class="f-rule"></div>
  <div class="f-links" style="left:130px">Request Medical Records<br>Upload Retrieved Record</div>
  <div class="f-links" style="left:335px">Chatroom<br>Query for Patient Records</div>
  <div class="f-links" style="left:544px;top:131px">Dashboard</div>
  <div class="copy">© Copyright VANTORA 2020 | All Rights Reserved.</div>
  <div class="f-mark"></div>
</footer>

</div>
</body>
</html>
```